Redesign start page for existing online shop

We are selling building material (chimneys and flue pipes) as well as fireplaces (stoves). For this online shop we need a new start page. The domain is brunnfeld-bauwaren.de. Here you can see the current design. We want a smoother design with just one banner in the middle instead of the three in the first row. The look has to be more professional and trustworthy. You can therefore play with the colors. We want to try some different orange instead of our yellow / orange color. A few more things: - The phone number has to be bigger and more highlighted - So the 5 advantages at the top should be shown in a different way - New design for the products below - New footer

Target Market(s)

Germany and other countries in Europe.

Industry/Entity Type

Home Builder

Number of Pages Required

1 page

Other font styles liked:
• Please se the font on our current site.

Colors
f78f20
f68d4c

Requirements
Must have
• - Clear design - Trustworthy look - All elements Which are now shown shoulderstand be still there after redesigning -
Nice to have
• - See the Following sites to have a clou about our wishes: kalvesto.de flinkrabe.de

```html
<!DOCTYPE html>
<html lang="de">
<head>
<meta charset="utf-8">
<title>Brunnfeld Bauwaren – Startseite</title>
<link rel="stylesheet" href="https://fonts.googleapis.com/css2?family=Open+Sans:wght@400;600;700;800&display=swap">
<style>
:root{
  --orange:#f78f20;
  --orange-soft:#f68d4c;
  --ink:#333333;
  --muted:#777777;
  --line:#e2e2e2;
  --grey-bg:#f2f2f2;
  --dark:#3a3a3a;
  --darker:#2a2a2a;
  --darkest:#1f1f1f;
  --white:#ffffff;
}
*{box-sizing:border-box;margin:0;padding:0}
html,body{width:1200px;height:4380px;overflow:hidden}
body{font-family:"Open Sans",Arial,sans-serif;color:var(--ink);background:var(--white);position:relative}
.wrap{width:1030px;margin:0 auto;position:relative;height:100%}
a{color:inherit;text-decoration:none}

.topbar{height:35px;background:#f5f5f5;border-bottom:1px solid var(--line);font-size:11px;color:#666}
.topbar .wrap{display:flex;justify-content:space-between;align-items:center}
.topbar ul{list-style:none;display:flex}
.topbar li{padding:0 12px;border-right:1px solid #d5d5d5}
.topbar li:first-child{padding-left:0}
.topbar li:last-child{border-right:0;padding-right:0}

.header{height:96px;background:var(--white)}
.header .wrap{display:flex;align-items:center;justify-content:space-between}
.brand{display:flex;align-items:center;gap:12px}
.brand-mark{width:40px;height:40px;background:var(--orange);border-radius:4px}
.brand-name{font-size:27px;font-weight:800;line-height:1;color:#444;letter-spacing:.5px}
.header-right{display:flex;align-items:center;gap:44px}
.rating-badge{display:flex;align-items:center;gap:8px;width:150px;height:56px;background:#f4f4f4;border-radius:6px;padding:0 8px}
.rating-badge span{width:44px;height:44px;border-radius:50%;background:#d8d8d8}
.rating-badge i{flex:1;height:14px;background:#e3e3e3;border-radius:3px}
.callus{display:flex;align-items:center;gap:12px}
.callus .ic{width:46px;height:46px;border-radius:50%;background:var(--orange);display:flex;align-items:center;justify-content:center}
.callus small{display:block;font-size:13px;color:var(--muted);font-weight:600}
.callus strong{display:block;font-size:25px;font-weight:800;color:var(--ink);line-height:1.1}

.mainnav{height:56px;background:var(--orange)}
.mainnav .wrap{display:flex;align-items:center;justify-content:space-between}
.mainnav ul{list-style:none;display:flex;height:56px}
.mainnav li{display:flex;align-items:center;padding:0 28px;color:var(--white);font-weight:700;font-size:16px;gap:6px}
.mainnav li.active{background:#e07c12}
.mainnav li:first-child{padding-left:24px}
.search{width:290px;height:34px;background:var(--white);border-radius:2px;display:flex;align-items:center;justify-content:space-between;padding:0 12px;font-size:13px;color:#888}

.hero{height:513px;position:relative;overflow:hidden}
.hero-visual{position:absolute;inset:0;background:linear-gradient(100deg,#6f6a63 0%,#a29a90 28%,#c9c2b6 50%,#8f7a63 72%,#5a4a3c 100%)}
.hero-title{position:absolute;right:80px;top:330px;width:660px;text-align:right;color:var(--white);font-size:33px;font-weight:800;line-height:1.25;text-shadow:0 2px 6px rgba(0,0,0,.55)}
.hero-arrow{position:absolute;top:238px;width:34px;height:34px;border-radius:50%;background:#222;display:flex;align-items:center;justify-content:center}
.hero-arrow.prev{left:22px}
.hero-arrow.next{right:22px}

.clients{height:147px;border-bottom:1px solid var(--line)}
.clients .wrap{display:flex;align-items:center}
.clients h2{font-size:27px;font-weight:700;width:235px;color:#333}
.client-list{display:flex;flex:1;list-style:none}
.client-list li{flex:1;height:64px;display:flex;align-items:center;justify-content:center;gap:8px;border-left:1px solid var(--line);font-size:22px;font-weight:700;color:#6a6a6a}
.client-list li:last-child{border-right:1px solid var(--line)}
.client-list li b{width:14px;height:14px;background:#9a9a9a;display:inline-block}

.benefits{height:325px;padding-top:58px}
.benefit-list{display:flex;gap:6px;list-style:none}
.benefit{flex:1;height:210px;background:var(--orange);position:relative;text-align:center;padding:70px 22px 0;color:var(--white)}
.benefit .badge{position:absolute;top:-44px;left:50%;margin-left:-44px;width:88px;height:88px;border-radius:50%;background:#3a3a3a;border:5px solid var(--white);display:flex;align-items:center;justify-content:center}
.benefit h3{font-size:16px;font-weight:800;line-height:1.25}
.benefit p{font-size:12px;line-height:1.4;margin-top:12px;font-weight:600;color:#fff3e4}

.how{height:525px;background:var(--grey-bg);padding-top:40px}
.section-title{text-align:center;font-size:29px;font-weight:700;color:#333}
.section-title em{font-style:normal;color:var(--orange)}
.steps{display:flex;list-style:none;margin-top:40px}
.step{flex:1;text-align:center}
.step .circle{width:140px;height:140px;border-radius:50%;background:var(--white);border:6px solid #e6e6e6;margin:0 auto;display:flex;align-items:center;justify-content:center}
.step h4{font-size:18px;font-weight:600;margin-top:20px;line-height:1.3}
.cta{display:flex;justify-content:center;align-items:center;gap:30px;margin-top:52px}
.cta p{font-size:25px;font-weight:700;color:#444}
.btn{background:var(--orange);color:var(--white);font-weight:700;font-size:16px;padding:13px 30px;border-radius:3px}

.products{height:405px;padding-top:80px;position:relative}
.product-list{display:flex;gap:44px;list-style:none}
.product{flex:1;border:1px solid var(--line);background:var(--white);height:280px;position:relative}
.product .shot{height:175px;margin:14px;background:linear-gradient(160deg,#f4f4f4,#cfcfcf)}
.product h5{font-size:15px;font-weight:600;text-align:center;margin-top:8px}
.product .buy{position:absolute;left:0;right:0;bottom:0;height:40px;border-top:1px solid var(--line);display:flex}
.product .price{flex:1;display:flex;align-items:center;padding-left:12px;font-size:14px;font-weight:700}
.product .go{background:var(--orange);color:var(--ink);font-size:12px;font-weight:800;display:flex;align-items:center;padding:0 14px}
.slide-btn{position:absolute;top:232px;width:30px;height:40px;background:#3a3a3a;display:flex;align-items:center;justify-content:center}
.slide-btn.prev{left:0}
.slide-btn.next{right:0}

.info{height:1385px;background:var(--dark);padding-top:42px;color:#d6d6d6}
.info .wrap{width:1030px}
.info h2{font-size:24px;font-weight:400;color:var(--orange);line-height:1.35}
.info h3{font-size:24px;font-weight:400;color:var(--white);margin-top:46px;line-height:1.3}
.info p{font-size:13px;line-height:1.65;margin-top:14px;color:#cfcfcf}

.trust{height:340px;padding-top:46px}
.trust-cols{display:flex;gap:70px;margin-top:56px}
.trust-item{flex:1;display:flex;gap:26px;align-items:center}
.trust-item .seal{width:110px;height:110px;border-radius:50%;background:#ececec;border:4px solid var(--orange);flex:none}
.trust-item p{font-size:14px;line-height:1.6;color:#555}

.payments{height:250px;background:var(--grey-bg);padding-top:40px}
.pay-list{display:flex;justify-content:center;gap:20px;list-style:none;margin-top:52px}
.pay-list li{width:100px;height:62px;background:var(--white);border:1px solid #d8d8d8;border-radius:4px;display:flex;align-items:center;justify-content:center;font-size:15px;font-weight:700;color:#555;text-align:center;line-height:1.1}

.footer{height:253px;background:var(--darker);color:#bdbdbd;padding-top:24px}
.footer .wrap{display:flex;gap:40px}
.footer h4{font-size:20px;font-weight:400;color:var(--white);padding-bottom:10px;border-bottom:1px solid #444;margin-bottom:14px}
.quick{width:300px}
.quick ul{list-style:none;columns:2;font-size:13px;line-height:2.4}
.quick li::before{content:"› ";color:var(--orange)}
.contact{flex:1}
.contact-grid{display:flex;gap:60px;font-size:13px;line-height:1.6}
.contact-grid strong{color:var(--white)}
.contact-row{display:flex;align-items:center;gap:10px;margin-bottom:14px}
.contact-row .dot{width:22px;height:22px;border-radius:50%;border:1px solid #777;flex:none}
.bottombar{height:35px;background:var(--darkest);color:#999;font-size:12px}
.bottombar .wrap{display:flex;justify-content:space-between;align-items:center}
.social{display:flex;gap:8px;list-style:none}
.social li{width:20px;height:20px;border-radius:50%;background:#555}
</style>
</head>
<body>

<div class="topbar">
  <div class="wrap">
    <ul><li>In 5 min zum Angebot</li><li>Fahrende marken</li><li>Mit uns förderung erhalten</li></ul>
    <ul><li>Standorte</li><li>für händler</li><li>Installateure</li></ul>
  </div>
</div>

<header class="header">
  <div class="wrap">
    <div class="brand"><span class="brand-mark"></span><span class="brand-name">BRUNNFELD<br>BAUWAREN</span></div>
    <div class="header-right">
      <div class="rating-badge" role="img" aria-label="Kundenbewertung"><span></span><i></i></div>
      <div class="callus">
        <span class="ic"><svg width="22" height="22" viewBox="0 0 24 24"><path fill="#fff" d="M6.6 10.8a15.1 15.1 0 0 0 6.6 6.6l2.2-2.2c.3-.3.7-.4 1-.2 1.1.4 2.3.6 3.6.6.6 0 1 .4 1 1V20c0 .6-.4 1-1 1C10.6 21 3 13.4 3 4c0-.6.4-1 1-1h3.5c.6 0 1 .4 1 1 0 1.3.2 2.5.6 3.6.1.3 0 .7-.2 1z"/></svg></span>
        <div><small>Call Us</small><strong>0800 5120 640</strong></div>
      </div>
    </div>
  </div>
</header>

<nav class="mainnav">
  <div class="wrap">
    <ul>
      <li class="active">Home</li>
      <li>Online-Shop ▾</li>
      <li>Services ▾</li>
      <li>Jobs</li>
      <li>Kontakt</li>
    </ul>
    <div class="search">Search <svg width="14" height="14" viewBox="0 0 24 24"><circle cx="10" cy="10" r="7" fill="none" stroke="#888" stroke-width="2.5"/><path d="M15 15l6 6" stroke="#888" stroke-width="2.5"/></svg></div>
  </div>
</nav>

<section class="hero">
  <div class="hero-visual" role="img" aria-label="Handwerker montiert eine Heiztherme an einer Backsteinwand"></div>
  <h1 class="hero-title">We Are Selling Building Material<br>(Chimneys And Flue Pipes) As Well As<br>Fire Places (stoves).</h1>
  <span class="hero-arrow prev"><svg width="12" height="12" viewBox="0 0 12 12"><path d="M8 1L3 6l5 5" fill="none" stroke="#fff" stroke-width="2"/></svg></span>
  <span class="hero-arrow next"><svg width="12" height="12" viewBox="0 0 12 12"><path d="M4 1l5 5-5 5" fill="none" stroke="#fff" stroke-width="2"/></svg></span>
</section>

<section class="clients">
  <div class="wrap">
    <h2>Our Clients</h2>
    <ul class="client-list">
      <li>Norvia</li>
      <li>Kestrel Bau</li>
      <li><b></b>Ostwerk</li>
      <li>Lindhof</li>
      <li>Tavora</li>
    </ul>
  </div>
</section>

<section class="benefits">
  <div class="wrap">
    <ul class="benefit-list">
      <li class="benefit">
        <span class="badge"><svg width="36" height="36" viewBox="0 0 24 24"><rect x="5" y="3" width="14" height="18" rx="1" fill="none" stroke="#fff" stroke-width="1.8"/><path d="M8 8h8M8 12h8M8 16h5" stroke="#fff" stroke-width="1.8"/></svg></span>
        <h3>Verbindliches Heizungs-Angebot sofort!</h3>
        <p>Geben Sie nur wenige Eckdaten zu Ihrem Haus in unser Formular ein.</p>
      </li>
      <li class="benefit">
        <span class="badge"><svg width="36" height="36" viewBox="0 0 24 24"><path d="M4 20l9-9M14 4l6 6-3 3-6-6z" fill="none" stroke="#fff" stroke-width="1.8"/><path d="M4 4l16 16" stroke="#fff" stroke-width="1.8"/></svg></span>
        <h3>Mehr als 30 Jahre Meisterqualität!</h3>
        <p>Erfahrung und Kompetenz sind der Garant für einen sauberen Einbau.</p>
      </li>
      <li class="benefit">
        <span class="badge"><svg width="36" height="36" viewBox="0 0 24 24"><rect x="4" y="4" width="16" height="16" rx="2" fill="none" stroke="#fff" stroke-width="1.8"/><path d="M8 7v10M12 7v10M16 7v10" stroke="#fff" stroke-width="1.8"/></svg></span>
        <h3>Neue Heizung bereits ab 39 € im Monat!</h3>
        <p>Die neue, umweltfreundliche und sparsame Heizung zum Festpreis.</p>
      </li>
      <li class="benefit">
        <span class="badge"><svg width="36" height="36" viewBox="0 0 24 24"><circle cx="12" cy="12" r="8" fill="none" stroke="#fff" stroke-width="1.8"/><path d="M8 12l3 3 5-6" fill="none" stroke="#fff" stroke-width="1.8"/></svg></span>
        <h3>10 Jahre Garantie auf Ihre neue Heizung!</h3>
        <p>Wir vertrauen Qualität und bieten Ihnen daher die volle Garantie.</p>
      </li>
    </ul>
  </div>
</section>

<section class="how">
  <div class="wrap">
    <h2 class="section-title">So <em>Funktioniert's</em></h2>
    <ul class="steps">
      <li class="step">
        <div class="circle"><svg width="64" height="64" viewBox="0 0 64 64"><rect x="6" y="22" width="52" height="28" rx="4" fill="#4a4a4a"/><g fill="#fff"><rect x="12" y="28" width="6" height="5"/><rect x="21" y="28" width="6" height="5"/><rect x="30" y="28" width="6" height="5"/><rect x="39" y="28" width="6" height="5"/><rect x="48" y="28" width="4" height="5"/><rect x="18" y="40" width="28" height="5"/></g><path d="M32 22v-8h10" fill="none" stroke="#f78f20" stroke-width="3"/></svg></div>
        <h4>Daten Online<br>Eingeben</h4>
      </li>
      <li class="step">
        <div class="circle"><svg width="64" height="64" viewBox="0 0 64 64"><path d="M14 50L50 14" stroke="#4a4a4a" stroke-width="8"/><path d="M46 50L20 14" stroke="#f78f20" stroke-width="6"/><path d="M16 10l4 4" stroke="#4a4a4a" stroke-width="6"/></svg></div>
        <h4>Aufmaß und beratung durch<br>kundenberater</h4>
      </li>
      <li class="step">
        <div class="circle"><svg width="64" height="64" viewBox="0 0 64 64"><rect x="16" y="8" width="32" height="46" rx="2" fill="none" stroke="#4a4a4a" stroke-width="3"/><path d="M22 20h20M22 28h20M22 36h14" stroke="#4a4a4a" stroke-width="3"/><circle cx="44" cy="48" r="8" fill="#f78f20"/></svg></div>
        <h4>Angebot von 2<br>Werkprofi Handwerken</h4>
      </li>
      <li class="step">
        <div class="circle"><svg width="64" height="64" viewBox="0 0 64 64"><rect x="8" y="26" width="48" height="26" rx="3" fill="#4a4a4a"/><path d="M24 26v-6h16v6" fill="none" stroke="#4a4a4a" stroke-width="3"/><rect x="8" y="34" width="48" height="4" fill="#f78f20"/></svg></div>
        <h4>Ausfuhrung</h4>
      </li>
    </ul>
    <div class="cta"><p>Jetzt unverbindlich eine anfrage stellen!</p><a class="btn">Anfrage stellen</a></div>
  </div>
</section>

<section class="products">
  <div class="wrap">
    <ul class="product-list">
      <li class="product"><div class="shot" role="img" aria-label="Edelstahl-Schornsteinverlängerung"></div><h5>Schornsteinverlängerung</h5><div class="buy"><span class="price">ab € 63,00</span><span class="go">JETZT ANSEHEN</span></div></li>
      <li class="product"><div class="shot" role="img" aria-label="Schornsteinabdeckung aus Edelstahl"></div><h5>Schornsteinabdeckung</h5><div class="buy"><span class="price">ab € 63,00</span><span class="go">JETZT ANSEHEN</span></div></li>
      <li class="product"><div class="shot" role="img" aria-label="Wanddurchführung mit Rohr"></div><h5>Wanddurchführung</h5><div class="buy"><span class="price">ab € 63,00</span><span class="go">JETZT ANSEHEN</span></div></li>
      <li class="product"><div class="shot" role="img" aria-label="Schwarzes Ofenrohr mit Bogen"></div><h5>Ofenrohr</h5><div class="buy"><span class="price">ab € 63,00</span><span class="go">JETZT ANSEHEN</span></div></li>
    </ul>
  </div>
  <span class="slide-btn prev"><svg width="10" height="12" viewBox="0 0 10 12"><path d="M8 0L1 6l7 6z" fill="#fff"/></svg></span>
  <span class="slide-btn next"><svg width="10" height="12" viewBox="0 0 10 12"><path d="M2 0l7 6-7 6z" fill="#fff"/></svg></span>
</section>

<section class="info">
  <div class="wrap">
    <h2>Edelstahlschornsteine, Schornsteinverlängerungen, Ofenrohre und Schornstein Zubehör – alles bei brunnfeld-bauwaren.de günstig kaufen.</h2>
    <p>Kann ich einen Edelstahlschornstein im Internet kaufen? Diese Frage haben Sie sich bestimmt noch nie gestellt. Bei anderen Waren ist das eine Selbstverständlichkeit, aber bei einem Edelstahlkamin denkt man zunächst nicht ans Onlineshopping. Dabei gibt es schon seit einigen Jahren diverse Plattformen, die sich rund um das Thema Edelstahlschornstein spezialisiert haben. Allerdings betreiben diese Anbieter ihre Webshops nur nebenher. Dies spiegelt sich in der schlechten Benutzerfreundlichkeit und der teilweise stark veralteten Technik der Seiten wieder. Unser Shop für Edelstahlschornsteine ist hier einen neuen Weg gegangen. Das Ziel war es, einen Onlineshop für Edelstahlschornsteine und Schornstein Zubehör auf die Beine zu stellen, der nicht nur professionell und nach dem neuesten Stand der Technik aufgebaut ist, sondern Ihnen auch die Sicherheit und Usability bietet, die Sie von großen Onlineplattformen anderer Branchen gewohnt sind. Mit einer effizienten Organisation, moderner Technik und jahrelanger Erfahrung mit dem Produkt Edelstahlschornstein konnte dieser Anspruch erfüllt werden. Beste Usability, geprüfter Datenschutz, hochwertige Waren und eine kompetente telefonische Beratung runden Ihr Einkaufserlebnis bei brunnfeld-bauwaren.de ab.</p>

    <h3>Edelstahlschornstein, Schornstein Bausatz und Edelstahlkamin – alles aus einer Hand.</h3>
    <p>Ob Sie einen doppelwandigen Edelstahlschornstein, eine Schornsteinsanierung für Ihren alten gemauerten Kamin oder einen Schornstein Bausatz für Ihr Haus suchen: hier werden Sie fündig. Bei uns finden Sie eine große Auswahl an in Deutschland hergestellter Edelstahlschornsteine des Herstellers Harlander. Diese Schornsteine werden nach modernsten Produktionsmethoden aus hochwertigem V4A Edelstahl hergestellt und unterliegen strengsten Qualitätskontrollen. Die Harlander GmbH gewährt Ihnen darüber hinaus auch eine Garantie von 25 Jahren auf jeden in diesem Onlineshop erworbenen Edelstahlschornstein. Ganz einfach: Sicherheit zum besten Preis!</p>
    <p>Und noch ein Tipp: Alle Schornsteine lassen sich wunderbar mit einem Ofenrohr von Harlander anschließen. Hier gibt es eine große Auswahl an verschiedenen Längen, Farben und Winkeln. Außerdem sind seit Kurzem auch isolierte Ofenrohre lieferbar. Diese doppelwandigen Ofenrohre verringern den Abstand der zu brennbaren Materialien eingehalten werden muss auf ein Minimum.</p>

    <h3>Schornsteinverlängerung und Kaminverlängerung günstig selbst aufbauen.</h3>
    <p>Aufgrund neuerer Verordnungen reicht die Höhe vieler bestehender Schornsteine nicht mehr aus. Durch bauliche Veränderungen der Umgebung oder auch vieler weiterer Gründe kann es dazu kommen, dass eine Schornsteinverlängerung nötig wird. In diesem Online Shop finden Sie Schornsteinverlängerungen in den Ausführungen doppelwandig oder einwandig. Jede Kaminverlängerung wird von Hand hergestellt und kann exakt nach Maß konfiguriert werden. Hier kaufen Sie eine Schornsteinverlängerung für die Ewigkeit.</p>

    <h3>Leichtbauschornstein F90 und eine Wanddurchführung: Brandschutz auf höchstem Niveau.</h3>
    <p>Ein Edelstahlschornstein eignet sich hervorragend als nachträglicher Abgasleitung neben einem bereits gemauerten Schornstein im Gebäude. Was aber, wenn Ihnen die Optik nicht zusagt oder Sie lieber den Schornstein im Inneren unsichtbar verschwinden lassen möchten? Dafür ist der Leichtbauschornstein von Harlander prädestiniert. In Verbindung mit einer feuerfesten Wanddurchführung haben Sie hier das perfekte Duo für einen sicheren Zusatzschornstein.</p>

    <h3>Schornsteinabdeckung, Kaminabdeckung und Kaminabdeckplatte aus Edelstahl nach Maß.</h3>
    <p>Ältere Schornsteinköpfe unterliegen starken Belastungen durch Witterungseinflüsse. Nach vielen Jahren des Regens, Sonnenscheins, der Kälte und der Wärme werden Schornsteinköpfe porös und beginnen zu bröckeln. Dann wird es höchste Zeit für eine Kaminabdeckplatte und eine Schornsteinabdeckung. Bei Kaminabdeckungen gibt es die bekannte Napoleonhaube und Meidinger Scheibe. Diese Modelle haben sich über viele Jahre bewährt und sind auf den meisten Gebäuden auch montiert. Bei uns finden Sie maßangefertigte Schornsteinabdeckungen aus Edelstahl oder Kupfer mit 25 Jahren Garantie.</p>

    <h3>Rauchsauger, Zugbegrenzer, Kamintüren und andere Spezialprodukte</h3>
    <p>Im Sortiment dieses Onlineshops finden Sie auch noch viele weitere Produkte rund um das Thema Schornstein und Abgastechnik. Hier wäre beispielsweise der Rauchsauger zu nennen. Ein sehr wichtiges Gerät, mit dem Sie den Schornsteinzug elektrisch verstärken können. Ebenfalls aus der Kategorie der Zugregelung und Zugverbesserung gibt es den Zugbegrenzer. Diese sogenannten Nebenluftvorrichtungen regeln rein mechanisch den Schornsteinzug. In manchen Fällen kann auch eine Abgasklappe notwendig werden. Neben der thermischen Abgasklappe finden Sie hier auch motorische Abgasklappen, die für Kaskaden oder Schornsteine mit Doppelbelegung notwendig sein können. Zu guter Letzt ist noch die Kamintüre zu erwähnen. Dieses Bauteil haben die meisten von Ihnen in der Schornsteinwange verbaut. Hier finden Sie passenden Ersatz, sollte es mal durchgerostet sein.</p>
    <p>Viel Spaß beim Einkaufen, wünscht Ihnen das Team von brunnfeld-bauwaren.de.</p>
  </div>
</section>

<section class="trust">
  <div class="wrap">
    <h2 class="section-title">Sicher <em>Einkaufen</em></h2>
    <div class="trust-cols">
      <div class="trust-item"><span class="seal" role="img" aria-label="Herkunftssiegel"></span><p>Wir bieten ausschließlich Waren von deutschen Markenherstellern an. Unser gesamtes Sortiment wird von Branchenführern hergestellt und unterliegt ständigen Qualitätskontrollen. Für Ihre Sicherheit nur das Beste zum fairen Preis.</p></div>
      <div class="trust-item"><span class="seal" role="img" aria-label="Garantiesiegel"></span><p>Um unserem Premiumanspruch und unserem Leistungsversprechen gerecht zu werden, erhalten Sie bei uns selbstverständlich auch 25 Jahre Garantie auf alle Edelstahlschornsteine und Edelstahlschornstein Bauteile.</p></div>
    </div>
  </div>
</section>

<section class="payments">
  <div class="wrap">
    <h2 class="section-title">Zahlungsarten</h2>
    <ul class="pay-list">
      <li>Cardora</li>
      <li>Vistra</li>
      <li>PayMint</li>
      <li>Direktly</li>
      <li>Vorkasse</li>
      <li>Orbis Card</li>
      <li>Last&shy;schrift</li>
    </ul>
  </div>
</section>

<footer class="footer">
  <div class="wrap">
    <div class="quick">
      <h4>Quick Links</h4>
      <ul>
        <li>Häufige Fragen</li><li>AGB</li><li>Lieferung &amp; Zahlung</li><li>Impressum</li><li>Blog</li>
        <li>Über uns</li><li>Widerruf</li><li>Datenschutz</li><li>Kontaktieren Sie uns</li><li>Glossar</li>
      </ul>
    </div>
    <div class="contact">
      <h4>Contact Us</h4>
      <div class="contact-grid">
        <div>
          <div class="contact-row"><span class="dot"></span><div><strong>Kastanienallee 14<br>81675 München<br>Deutschland</strong></div></div>
          <div><strong>Brunnfeld Bauwaren</strong><br>Durchschnittliche Bewertung: 4.71 (von 5).<br>Ermittelt aus 265 Bewertungen.</div>
        </div>
        <div>
          <strong>Kostenlose Beratung</strong>
          <div class="contact-row" style="margin-top:12px"><span class="dot"></span>08141 / 408 173 0</div>
          <div class="contact-row"><span class="dot"></span>Mo. - Fr. von 09:00 bis 18:00 Uhr</div>
          <div class="contact-row"><span class="dot"></span>info@brunnfeld-bauwaren.de</div>
        </div>
      </div>
    </div>
  </div>
</footer>

<div class="bottombar">
  <div class="wrap">
    <span>Copyright © 2011 - 2016 Feldmark GmbH. All Rights Reserved.</span>
    <ul class="social" aria-label="Soziale Netzwerke"><li></li><li></li><li></li><li></li><li></li></ul>
  </div>
</div>

</body>
</html>
```